Promotional Flyer for Iron Crane Dialogue

Design a promotional Flyer for Iron Crane Dialogue. Iron Crane Dialogue is a children and teen anti-bullying program. The program is delivered as a term program or as stand alone workshops. Target audience is parent and schools. The program can be delivered for different age groups; 6yr+ 9yrs+ 14yr+ The program will begin in 2017. Details are on the flyers and mock brochure. Bullying is a major problem in Australia for children and teens of all ages starting in primary school through to highschool. In extreme cases it may lead to suicide. I want to make a strong statement and reach out to families who want to help their children and teen by giving them skills and confidence needed to stand up to bullies. Trying to keep it to a one page or two page (back & Front). Need to maintain a martial art ethos but be modern and exciting to look at.
Updates

This is such an important project. I look forward to watching amazing layouts by designers who really see this much more than just another graphic design project but are invested in making a difference for the children and teens who will come through this program. The project is sponsored by Marrowvale karate in the Pilbara - Western Australia. check us out https://www.facebook.com/marrowvalekarateclub/ Thanks Rob

Target Market(s)

parents of children and teens, schools, mental health service providers, government, youth services

Industry/Entity Type

Mental Health

Font styles to use
Sans Serif

Requirements
Must have
• Must have Logos; Iron Crane Dialogue prominent. Must have lesson outline. Must have detail. Must have a martial art ethos Must clearly communicate this is anti-bullying.
Nice to have
• Color - strong anti-bullying message. Clear communication can be delivered in workshops or term based program.
Should not have
• Should not be boring. Not too wordy.

```html
<!DOCTYPE html>
<html lang="en">
<head>
<meta charset="utf-8">
<title>Bully Proof – Iron Crane Dialogue</title>
<link rel="stylesheet" href="https://fonts.googleapis.com/css2?family=Montserrat:wght@900&family=Barlow:wght@500;600&family=Barlow+Condensed:wght@600&family=Open+Sans:wght@400&display=swap">
<style>
  :root {
    --ink: #0b0b0b;
    --paper: #ffffff;
    --red: #e3222b;
    --blush: #f8c6b4;
    --text: #1d1d1d;
    --badge-red: #d8262e;
    --badge-blue: #2a4f9a;
    --badge-orange: #e8743a;
  }
  * { margin: 0; padding: 0; box-sizing: border-box; }
  html, body { width: 989px; height: 1200px; overflow: hidden; background: var(--paper); }
  .flyer { position: relative; width: 989px; height: 1200px; background: var(--paper); color: var(--text); }

  .headline { position: absolute; left: 22px; font-family: "Montserrat", sans-serif; font-weight: 900; color: var(--ink); font-size: 134px; line-height: 1; letter-spacing: -3px; }
  .headline--top { top: 22px; }
  .headline--bottom { top: 186px; }
  .tagline { position: absolute; left: 28px; top: 150px; font-family: "Barlow", sans-serif; font-weight: 600; font-size: 27px; color: var(--red); letter-spacing: 0.5px; }

  .intro { position: absolute; left: 549px; top: 35px; width: 440px; height: 297px; background: var(--ink); border-radius: 12px 0 0 12px; padding: 16px 26px 0 24px; color: var(--paper); font-family: "Open Sans", sans-serif; font-size: 18.6px; line-height: 23.4px; text-align: justify; hyphens: auto; }

  .brand { position: absolute; left: 36px; top: 362px; width: 920px; height: 150px; display: flex; align-items: center; gap: 40px; }
  .brand__mark { width: 140px; height: 140px; border-radius: 50%; background: var(--ink); flex: none; }
  .brand__name { font-family: "Montserrat", sans-serif; font-weight: 900; color: var(--ink); font-size: 68px; line-height: 0.98; letter-spacing: -1px; }

  .lessons { position: absolute; left: 0; top: 543px; width: 989px; height: 219px; background: var(--blush); }
  .lessons__title { position: absolute; left: 30px; top: 14px; font-family: "Barlow", sans-serif; font-weight: 600; font-size: 42px; color: var(--red); letter-spacing: 0.5px; }
  .lessons__list { position: absolute; top: 57px; list-style: none; font-family: "Barlow", sans-serif; font-weight: 500; font-size: 20px; color: var(--text); }
  .lessons__list--left { left: 35px; }
  .lessons__list--right { left: 502px; }
  .lessons__list li { display: flex; align-items: center; gap: 8px; height: 31.2px; }
  .tick { width: 19px; height: 19px; flex: none; }

  .links { position: absolute; left: 36px; top: 788px; font-family: "Open Sans", sans-serif; font-size: 22px; line-height: 30px; color: var(--ink); }
  .links__social { display: flex; align-items: center; gap: 6px; }
  .links__dot { width: 26px; height: 26px; border-radius: 50%; background: var(--red); display: inline-block; }

  .partners { position: absolute; left: 52px; top: 903px; display: flex; align-items: center; gap: 28px; }
  .partner { width: 80px; height: 80px; border-radius: 50%; }
  .partner--club { background: var(--badge-red); }
  .partner--program { background: var(--badge-orange); }
  .partner__name { font-family: "Open Sans", sans-serif; font-size: 34px; color: var(--badge-blue); letter-spacing: 0.5px; }

  .details { position: absolute; left: 0; top: 991px; width: 474px; height: 192px; background: var(--ink); border-radius: 0 12px 12px 0; padding: 18px 0 0 26px; color: var(--paper); font-family: "Barlow Condensed", sans-serif; font-weight: 600; font-size: 16.5px; line-height: 22.8px; }
  .details b { font-weight: 600; }

  .photo { position: absolute; left: 502px; top: 805px; width: 475px; height: 378px; background: linear-gradient(180deg, #f6f6f6 0%, #ececec 55%, #e2dcd6 100%); }
</style>
</head>
<body>
<main class="flyer">
  <h1>
    <span class="headline headline--top">BULLY</span>
    <span class="headline headline--bottom">PROOF</span>
  </h1>
  <p class="tagline">CONFIDENCE – COURAGE – CONTROL</p>

  <p class="intro">Iron Crane Dialogue provides anti-bullying workshops and term based programs that will engage, equip, and empower your child &amp; teen with skills and confidence needed to stop bullying and build effective communication skills. Iron Crane Dialogue combines the ethos of martial arts training with the teaching methods of the acclaimed "Stone &amp; River" antibullying program developed by the Veldman Institute in Holland.</p>

  <div class="brand">
    <span class="brand__mark"></span>
    <p class="brand__name">IRON CRANE<br>DIALOGUE</p>
  </div>

  <section class="lessons">
    <h2 class="lessons__title">KEY LESSONS</h2>
    <ul class="lessons__list lessons__list--left">
      <li><svg class="tick" viewBox="0 0 20 20"><rect x="1.5" y="3.5" width="15" height="15" rx="3" fill="none" stroke="#e3222b" stroke-width="2.4"/><path d="M5 10l4 4 9-11" fill="none" stroke="#e3222b" stroke-width="2.8" stroke-linecap="round"/></svg>Iron Crane Dialogue Code</li>
      <li><svg class="tick" viewBox="0 0 20 20"><rect x="1.5" y="3.5" width="15" height="15" rx="3" fill="none" stroke="#e3222b" stroke-width="2.4"/><path d="M5 10l4 4 9-11" fill="none" stroke="#e3222b" stroke-width="2.8" stroke-linecap="round"/></svg>Stone &amp; River Relationships</li>
      <li><svg class="tick" viewBox="0 0 20 20"><rect x="1.5" y="3.5" width="15" height="15" rx="3" fill="none" stroke="#e3222b" stroke-width="2.4"/><path d="M5 10l4 4 9-11" fill="none" stroke="#e3222b" stroke-width="2.8" stroke-linecap="round"/></svg>Foundations 4 Standing Strong</li>
      <li><svg class="tick" viewBox="0 0 20 20"><rect x="1.5" y="3.5" width="15" height="15" rx="3" fill="none" stroke="#e3222b" stroke-width="2.4"/><path d="M5 10l4 4 9-11" fill="none" stroke="#e3222b" stroke-width="2.8" stroke-linecap="round"/></svg>Breathing &amp; Balance Under Pressure</li>
      <li><svg class="tick" viewBox="0 0 20 20"><rect x="1.5" y="3.5" width="15" height="15" rx="3" fill="none" stroke="#e3222b" stroke-width="2.4"/><path d="M5 10l4 4 9-11" fill="none" stroke="#e3222b" stroke-width="2.8" stroke-linecap="round"/></svg>Self Defence (Persuasion &amp; Evasion)</li>
    </ul>
    <ul class="lessons__list lessons__list--right">
      <li><svg class="tick" viewBox="0 0 20 20"><rect x="1.5" y="3.5" width="15" height="15" rx="3" fill="none" stroke="#e3222b" stroke-width="2.4"/><path d="M5 10l4 4 9-11" fill="none" stroke="#e3222b" stroke-width="2.8" stroke-linecap="round"/></svg>Friend or Foe (Boundaries for All)</li>
      <li><svg class="tick" viewBox="0 0 20 20"><rect x="1.5" y="3.5" width="15" height="15" rx="3" fill="none" stroke="#e3222b" stroke-width="2.4"/><path d="M5 10l4 4 9-11" fill="none" stroke="#e3222b" stroke-width="2.8" stroke-linecap="round"/></svg>Don't Be a Bystander: How to Give and Get Help</li>
      <li><svg class="tick" viewBox="0 0 20 20"><rect x="1.5" y="3.5" width="15" height="15" rx="3" fill="none" stroke="#e3222b" stroke-width="2.4"/><path d="M5 10l4 4 9-11" fill="none" stroke="#e3222b" stroke-width="2.8" stroke-linecap="round"/></svg>3R's For Successful Relationships</li>
      <li><svg class="tick" viewBox="0 0 20 20"><rect x="1.5" y="3.5" width="15" height="15" rx="3" fill="none" stroke="#e3222b" stroke-width="2.4"/><path d="M5 10l4 4 9-11" fill="none" stroke="#e3222b" stroke-width="2.8" stroke-linecap="round"/></svg>Inner Compass: Navigating Relationships</li>
      <li><svg class="tick" viewBox="0 0 20 20"><rect x="1.5" y="3.5" width="15" height="15" rx="3" fill="none" stroke="#e3222b" stroke-width="2.4"/><path d="M5 10l4 4 9-11" fill="none" stroke="#e3222b" stroke-width="2.8" stroke-linecap="round"/></svg>Iron Crane Teamwork</li>
    </ul>
  </section>

  <div class="links">
    <p class="links__social"><span class="links__dot"></span>/marrowvalekarateclub</p>
    <p>learnbridge.com.au</p>
    <p>www.stoneandriverprogram.com</p>
  </div>

  <div class="partners">
    <span class="partner partner--club"></span>
    <span class="partner partner--program"></span>
    <span class="partner__name">LearnBridge</span>
  </div>

  <div class="details">
    <p><b>LOCATION:</b> Pinecrest Community Centre</p>
    <p><b>TIME:</b> Every Saturday morning/afternoon. (45min lessons)</p>
    <p><b>REGISTRATION:</b> Jan 2017 CLASS START: February 2017</p>
    <p><b>COST:</b> $150 per term + $50 Equipment</p>
    <p><b>AGES:</b> 6yrs+ 9yrs+ 14yrs+ (min 10 - max 20 per class)</p>
    <p><b>TRAINER:</b> Rob Calder (Stone&amp;River Facilitator / 3rd Dan Karate)</p>
    <p><b>CONTACT:</b> rob@ironcranedialogue.com or 0412345678</p>
  </div>

  <div class="photo" role="img" aria-label="Photo of four smiling children in white martial arts uniforms with green, red, yellow and white belts"></div>
</main>
</body>
</html>
```